1 Page Bio, describing our Mission to buy multifamily properties in Colorado Springs.

I am uploading a sample of an associate who is doing a similar thing in Tampa Florida. I will also upload an attempt by my assistant to make the flyer and I will upload 3 pictures to use, along with another document that has text to add. I want to be able to edit the document pretty easily inside a google doc. thanks, I want it to look clean and professional.

```html
<!DOCTYPE html>
<html lang="en">
<head>
<meta charset="utf-8">
<title>Acquiring Value-Add Multifamily Real Estate in Colorado Springs</title>
<link rel="stylesheet" href="https://fonts.googleapis.com/css2?family=Bebas+Neue&family=Montserrat:wght@400;500;600;700&display=swap">
<style>
:root{
  --teal:#0e6a62;
  --teal-dark:#0a524b;
  --navy:#1c2838;
  --ink:#2a2f36;
  --grey-band:#d9dcdf;
  --page:#f4f5f6;
  --footer-dark:#3c4148;
  --footer-blue:#4f6d93;
  --line:#9aa0a6;
}
*{margin:0;padding:0;box-sizing:border-box}
html,body{width:850px;height:1200px;overflow:hidden;background:#fff}
body{font-family:"Montserrat",sans-serif;color:var(--ink)}
.flyer{position:relative;width:850px;height:1200px;overflow:hidden;
  background:linear-gradient(180deg,#ffffff 0%,#f3f4f5 45%,#eef0f1 100%)}
.abs{position:absolute}
.display{font-family:"Bebas Neue",sans-serif;font-weight:400;letter-spacing:.5px}

/* hero */
.hero-art{position:absolute;left:0;top:0}
.brand-box{left:134px;top:0;width:218px;height:148px;background:var(--teal);
  display:flex;align-items:center;justify-content:center;gap:8px}
.brand-box .mark{width:12px;height:12px;border:2px solid #fff}
.brand-box .name{color:#fff;font-weight:600;font-size:17px;letter-spacing:1px}
.hero-title{left:20px;top:158px;width:462px;text-align:center;color:var(--navy);
  font-size:39px;line-height:47px}

/* right column */
.pillar{left:554px;width:290px}
.pillar .icon{position:absolute;left:0;top:0;width:40px;height:40px}
.pillar h3{margin-left:54px;color:var(--teal);font-size:21px;line-height:24px;padding-top:6px}
.pillar p{margin-left:56px;font-size:12px;line-height:15.5px;margin-top:3px;color:var(--ink)}

.swoosh{position:absolute;left:0;top:0}
.portrait{left:490px;top:290px;width:150px;height:150px;border-radius:50%;
  border:5px solid #fff;box-shadow:0 2px 8px rgba(0,0,0,.25);
  background:radial-gradient(circle at 50% 35%,#7b8c6e 0%,#4e5f4a 55%,#2f3a2e 100%)}
.portrait-caption{left:485px;top:410px}

.principals-title{left:519px;top:484px;color:var(--teal);font-size:30px}
.person{left:522px;width:320px}
.person h4{font-weight:500;font-size:17px;color:var(--ink);margin-bottom:6px}
.bullets{list-style:none}
.bullets li{position:relative;padding-left:11px;font-size:10.4px;line-height:13px}
.bullets li::before{content:"";position:absolute;left:1px;top:4px;width:5px;height:5px;border-radius:50%;background:#222}

.divider-v{left:496px;top:560px;width:1px;height:215px;background:#d3d6d9}

/* market */
.market-icon{left:394px;top:478px}
.market-title{left:200px;top:555px;width:256px;text-align:right;color:var(--teal);font-size:34px;line-height:40px}
.market-copy{left:60px;top:650px;width:396px;text-align:right;font-size:12.2px;line-height:15.5px}
.market-copy b{font-weight:700}

/* why sections */
.section-title{color:var(--teal);font-size:27px}
.dot-list{list-style:none}
.dot-list li{position:relative;padding-left:14px;font-size:12.2px;line-height:15.3px}
.dot-list li::before{content:"";position:absolute;left:1px;top:4.5px;width:6px;height:6px;border-radius:50%;background:#222}

/* advisors */
.rule{height:1px;background:var(--line)}
.rule::before,.rule::after{content:"";position:absolute;top:-2px;width:5px;height:5px;border-radius:50%;background:var(--line)}
.rule::before{left:-2px}.rule::after{right:-2px}
.advisor-photo{left:508px;width:83px;height:84px;border:1px solid #c9ccd0;
  background:linear-gradient(180deg,#f2f2f2 0%,#b9bcbf 60%,#6f7377 100%)}
.advisor{left:603px;width:222px}
.advisor h4{font-weight:500;font-size:17px;margin-bottom:2px}
.small-list{list-style:none}
.small-list li{position:relative;padding-left:5px;font-size:9.2px;line-height:12px}
.small-list li::before{content:"";position:absolute;left:0;top:4px;width:3px;height:3px;border-radius:50%;background:#222}
.small-list.just li{text-align:justify;margin-bottom:12px}

/* strategy */
.strategy-col{width:170px}
.strategy-col h5{font-family:"Bebas Neue",sans-serif;font-weight:400;font-size:18px;color:var(--navy);margin-bottom:6px}
.strategy-col ul{list-style:none}
.strategy-col li{position:relative;padding-left:8px;font-size:9.4px;line-height:12px}
.strategy-col li::before{content:"";position:absolute;left:0;top:4px;width:4px;height:4px;border-radius:50%;background:#222}
.col-sep{width:1px;background:#c9ccd0}

/* footer */
.footer{left:0;top:1152px;width:850px;height:48px;display:flex}
.footer .cta{width:192px;background:var(--footer-dark);color:#fff;font-weight:700;font-size:19px;
  display:flex;align-items:center;padding-left:18px}
.footer .info{flex:1;background:var(--footer-blue);color:#fff;position:relative}
.footer .names{position:absolute;left:16px;top:6px;font-size:15px;font-weight:500}
.footer .email{position:absolute;left:16px;top:27px;font-size:11.5px;display:flex;align-items:center;gap:4px}
.footer .phone{position:absolute;left:198px;top:8px;font-size:25px;font-weight:700;display:flex;align-items:center;gap:8px}
.footer .web{position:absolute;left:453px;top:18px;font-size:11px;letter-spacing:2.5px}
</style>
</head>
<body>
<div class="flyer">

  <!-- hero photo area with curved edge -->
  <svg class="hero-art" width="850" height="700" viewBox="0 0 850 700" role="img" aria-label="Photo of a three-storey blue-sided apartment complex with a fenced pool and landscaped lawn under a blue sky">
    <defs>
      <linearGradient id="heroFill" x1="0" y1="0" x2="0" y2="1">
        <stop offset="0" stop-color="#3f78b6"/>
        <stop offset=".22" stop-color="#86afd8"/>
        <stop offset=".4" stop-color="#c7d9ea"/>
        <stop offset=".46" stop-color="#5d7593"/>
        <stop offset=".62" stop-color="#3f5877"/>
        <stop offset=".74" stop-color="#6b7b6a"/>
        <stop offset=".86" stop-color="#7f9a62"/>
        <stop offset="1" stop-color="#5f7d45"/>
      </linearGradient>
      <linearGradient id="bandFill" x1="0" y1="0" x2="1" y2="0">
        <stop offset="0" stop-color="#e1e3e5"/>
        <stop offset="1" stop-color="#c9cdd1"/>
      </linearGradient>
    </defs>
    <path d="M0,0 H496 V330 C410,380 240,440 0,545 Z" fill="url(#heroFill)"/>
    <path d="M0,545 C240,440 410,380 496,330 L496,348 C400,420 230,540 55,650 Z" fill="url(#bandFill)"/>
  </svg>

  <div class="abs brand-box"><span class="mark"></span><span class="name">CRESTLINE HOME</span></div>
  <h1 class="abs hero-title display">Acquiring Value-Add Multifamily<br>Real Estate in Colorado Springs</h1>

  <!-- teal swoosh -->
  <svg class="swoosh" width="850" height="460" viewBox="0 0 850 460" aria-hidden="true">
    <path d="M520,330 C600,410 700,420 850,282 L850,300 C770,385 720,432 700,432 C650,432 610,405 520,330 Z" fill="var(--teal)"/>
  </svg>

  <!-- mission / values / process -->
  <div class="abs pillar" style="top:36px">
    <svg class="icon" viewBox="0 0 40 40" aria-hidden="true"><circle cx="20" cy="20" r="18.5" fill="none" stroke="var(--teal)" stroke-width="2"/><circle cx="20" cy="20" r="11" fill="none" stroke="var(--teal)" stroke-width="2"/><circle cx="20" cy="20" r="5" fill="none" stroke="var(--teal)" stroke-width="2"/><circle cx="20" cy="20" r="1.6" fill="var(--teal)"/><path d="M20 20 L29 11 M26 10 L30 10 L30 14" stroke="var(--teal)" stroke-width="2" fill="none"/></svg>
    <h3 class="display">Our Mission</h3>
    <p>To create a family business<br>by purchasing Multifamily<br>Residences, one at a time.</p>
  </div>
  <div class="abs pillar" style="top:121px">
    <svg class="icon" viewBox="0 0 40 40" aria-hidden="true"><circle cx="20" cy="20" r="18.5" fill="none" stroke="var(--teal)" stroke-width="2"/><path d="M8 17 L14 14 L20 17 L26 14 L32 17 L26 24 L22 27 L18 24 Z" fill="var(--teal)"/></svg>
    <h3 class="display">Our Values</h3>
    <p>To provide a white glove experience<br>to allresidences with a clean,<br>safe, and fun environment.</p>
  </div>
  <div class="abs pillar" style="top:207px">
    <svg class="icon" viewBox="0 0 40 40" aria-hidden="true"><circle cx="20" cy="20" r="18.5" fill="none" stroke="var(--teal)" stroke-width="2"/><circle cx="20" cy="20" r="8" fill="none" stroke="var(--teal)" stroke-width="5" stroke-dasharray="3 2.3"/><circle cx="20" cy="20" r="3" fill="var(--teal)"/></svg>
    <h3 class="display">The Process</h3>
    <p>Buy right, manage right,<br>and finance right.</p>
  </div>

  <!-- principals portrait -->
  <div class="abs portrait" role="img" aria-label="Photo of the two principals standing outdoors among trees"></div>
  <svg class="abs portrait-caption" width="170" height="60" viewBox="0 0 170 60" aria-hidden="true">
    <defs><path id="captionArc" d="M20,6 Q85,52 150,6"/></defs>
    <text font-family="Montserrat, sans-serif" font-size="12" fill="#2a2f36"><textPath href="#captionArc" startOffset="50%" text-anchor="middle">Russell &amp; Clark Marlow</textPath></text>
  </svg>

  <h2 class="abs principals-title display">Principals:</h2>
  <div class="abs person" style="top:528px">
    <h4>Russell Marlow</h4>
    <ul class="bullets">
      <li>Licensed Colorado Real Estate Agent 18 years.</li>
      <li>Broker-Owner of two HomeKey Realty Franchises 7 and 2 Years.</li>
      <li>Real Estate investing for 5 years.</li>
      <li>Member of Keystone Profits Academy.</li>
      <li>Married 24 years to Bonnie, parenting 10 children together.</li>
      <li>Appeared on Nate and Leo's Multifamily Hour podcast Episode 43</li>
      <li>$2M portfolio.</li>
    </ul>
  </div>
  <div class="abs person" style="top:679px">
    <h4>Clark Marlow</h4>
    <ul class="bullets">
      <li>Retired Electrical Engineer.</li>
      <li>Active Real Estate Investor/Consultant.</li>
      <li>Net worth over $4M</li>
      <li>15 Grandchildren.</li>
    </ul>
  </div>

  <div class="abs divider-v"></div>

  <!-- market -->
  <svg class="abs market-icon" width="58" height="58" viewBox="0 0 58 58" aria-hidden="true">
    <g fill="none" stroke="var(--teal)" stroke-width="2.2">
      <path d="M4 26 L29 4 L54 26"/><path d="M40 10 V5 H46 V15"/>
      <path d="M10 22 V54 H48 V22"/><path d="M2 54 H56"/>
      <path d="M17 52 V40 M24 52 V36 M31 52 V40 M38 52 V32"/>
      <path d="M15 34 L24 27 L31 31 L40 22 M36 22 H40 V26"/>
    </g>
  </svg>
  <h2 class="abs market-title display">The Market:<br>Colorado Springs</h2>
  <div class="abs market-copy">
    Projected job growth of nearly 50%<br>
    Below average unemployment rates.<br>
    Above-average incomes.<br>
    Solid economy, military, aerospace, electronics industry,<br>
    and tourism.<br>
    <b>The Target :</b> B and C class assets located in Colorado Springs<br>
    or nearby submarkets.
  </div>

  <!-- why sections -->
  <h2 class="abs section-title display" style="left:40px;top:798px">Why Multifamily?</h2>
  <ul class="abs dot-list" style="left:24px;top:841px;width:220px">
    <li>Earn monthly cashflow</li>
    <li>Huge TAX Benefits</li>
    <li>Passive Income</li>
    <li>Historically Stable Investments</li>
    <li>Economies of Scale</li>
    <li>Housing is an enduring need</li>
  </ul>
  <h2 class="abs section-title display" style="left:246px;top:798px">Why Colorado Springs?</h2>
  <ul class="abs dot-list" style="left:239px;top:841px;width:240px">
    <li>Strong Job Growth 2.91%</li>
    <li>Robust Population Growth 1.95%</li>
    <li>20.5% Population increase by 2030</li>
    <li>Low Unemployment Rate 2.9%</li>
    <li>Many large firms relocating to<br>Colorado Spring</li>
  </ul>

  <!-- advisors -->
  <div class="abs rule" style="left:526px;top:808px;width:60px"></div>
  <h2 class="abs section-title display" style="left:638px;top:791px;font-size:30px">Advisors</h2>
  <div class="abs rule" style="left:756px;top:808px;width:60px"></div>

  <div class="abs advisor-photo" style="top:846px" role="img" aria-label="Black and white headshot of advisor"></div>
  <div class="abs advisor" style="top:843px">
    <h4>Dean Lockwood</h4>
    <ul class="small-list">
      <li>General partner on 103 Apartments</li>
      <li>Acquiring 101 more apartments in Q1 - 2020</li>
      <li>Flips 4-8 houses a year</li>
      <li>Active member in the Nate &amp; Leo Community</li>
      <li>Accountability coach</li>
    </ul>
  </div>

  <div class="abs advisor-photo" style="top:982px" role="img" aria-label="Black and white headshot of advisor"></div>
  <div class="abs advisor" style="top:955px">
    <h4>Brent Hale</h4>
    <ul class="small-list just">
      <li>Brent is the owner/operator of Summit Residential Group and Summit Residential Management</li>
      <li>He has been in the real estate business for 13 years and has created a portfolio of over 1000 units while growing Summit Management with team of 15 staff members.</li>
      <li>He has taught real estate for the past 6 years and has dozens of highly successful students. Brent useshis extensive real estate experience to teach his students the "real" side of real estate.</li>
    </ul>
  </div>

  <!-- investment strategy -->
  <div class="abs rule" style="left:28px;top:987px;width:96px"></div>
  <h2 class="abs section-title display" style="left:138px;top:971px;font-size:30px">Investment Strategy</h2>
  <div class="abs rule" style="left:356px;top:987px;width:98px"></div>

  <div class="abs strategy-col" style="left:26px;top:1016px">
    <h5>Acquire</h5>
    <ul>
      <li>Purchase Underperforming</li>
      <li>Apartment Communities</li>
      <li>Mom and Pop Characteristies</li>
      <li>Class B and C Buildings</li>
      <li>20-50 units</li>
      <li>Deferred maintenance<br>Value-Add opportunity</li>
    </ul>
  </div>
  <div class="abs col-sep" style="left:192px;top:1022px;height:110px"></div>
  <div class="abs strategy-col" style="left:206px;top:1016px">
    <h5>Reposition:</h5>
    <ul>
      <li>Hire professional<br>management team</li>
      <li>Stabilize the property</li>
      <li>Fill vacancies</li>
      <li>implement RUBS</li>
      <li>Change fee structure</li>
      <li>Raise remaining rents</li>
    </ul>
  </div>
  <div class="abs col-sep" style="left:333px;top:1022px;height:110px"></div>
  <div class="abs strategy-col" style="left:342px;top:1016px">
    <h5>Refinance &amp; Proceeds:</h5>
    <ul>
      <li style="margin-bottom:12px">Refinance the property<br>and roll proceeds into<br>the next.</li>
      <li>Sell the property and<br>cash out or roll into the<br>next property.</li>
    </ul>
  </div>

  <!-- footer -->
  <div class="abs footer">
    <div class="cta">Parther with us</div>
    <div class="info">
      <div class="names">Russell &amp; Clark Marlow</div>
      <div class="email">
        <svg width="10" height="8" viewBox="0 0 10 8" aria-hidden="true"><rect x=".5" y=".5" width="9" height="7" fill="#fff"/><path d="M.5 .8 L5 4.5 L9.5 .8" stroke="var(--footer-blue)" fill="none"/></svg>
        rmarlow@example.com
      </div>
      <div class="phone">
        <svg width="24" height="24" viewBox="0 0 24 24" aria-hidden="true"><circle cx="12" cy="12" r="10.5" fill="none" stroke="#fff" stroke-width="2"/><path d="M8.3 6.5 L10.3 6.2 L11.2 9 L9.9 10.1 C10.6 11.7 11.9 13.1 13.6 13.9 L14.8 12.6 L17.6 13.6 L17.3 15.6 C12.5 16.1 7.7 11.3 8.3 6.5 Z" fill="#fff"/></svg>
        719-555-0148
      </div>
      <div class="web">www.marlowhomes.com</div>
    </div>
  </div>

</div>
</body>
</html>
```